Lanterns and Ledgers

To design a cd cover. The cd will contain original songs written about life, love, and heartbreak, and cover a roughly 40 year period of songwriting..
The songs are timely yet eternal...cover art should convey contemporary themes yet refer to the last 50 or so years of musical and societal happenings.

```html
<!DOCTYPE html>
<html lang="en">
<head>
<meta charset="utf-8">
<title>My Life My Love — 40 Year Collection</title>
<link href="https://fonts.googleapis.com/css2?family=Great+Vibes&family=Roboto:wght@700&display=swap" rel="stylesheet">
<style>
  :root {
    --backdrop: #3f3a6e;
    --band: #3f3a6e;
    --spindle-red: #e02628;
    --title-coral: #e8685a;
    --title-white: #ffffff;
    --sky-light: #fff6d8;
    --sky-gold: #ffc63a;
    --sky-orange: #f39a3a;
    --sea-haze: #e6dce8;
    --street-grey: #8d9391;
    --street-dark: #5f6665;
    --dress-red: #d93a45;
  }
  html, body {
    margin: 0;
    padding: 0;
    width: 1200px;
    height: 1000px;
    overflow: hidden;
    background: var(--backdrop);
  }
  .cover {
    display: block;
    width: 1200px;
    height: 1000px;
  }
  .title-script {
    font-family: "Great Vibes", cursive;
    text-anchor: middle;
  }
  .title-life { fill: var(--title-coral); opacity: 0.88; }
  .title-love { fill: var(--title-white); }
  .span-label {
    font-family: "Roboto", Arial, sans-serif;
    font-weight: 700;
    fill: var(--title-white);
    text-anchor: middle;
    letter-spacing: 1px;
  }
</style>
</head>
<body>
<svg class="cover" viewBox="0 0 1200 1000" xmlns="http://www.w3.org/2000/svg">
  <defs>
    <clipPath id="disc-shape">
      <circle cx="600" cy="500" r="398"/>
    </clipPath>
    <linearGradient id="sunset-tones" x1="0" y1="0" x2="0" y2="1">
      <stop offset="0" stop-color="var(--sky-light)"/>
      <stop offset="0.35" stop-color="var(--sky-gold)"/>
      <stop offset="0.6" stop-color="var(--sky-orange)"/>
      <stop offset="1" stop-color="var(--sea-haze)"/>
    </linearGradient>
    <radialGradient id="sun-glow" cx="0.45" cy="0.45" r="0.5">
      <stop offset="0" stop-color="#fff3a0" stop-opacity="0.9"/>
      <stop offset="1" stop-color="#fff3a0" stop-opacity="0"/>
    </radialGradient>
    <linearGradient id="street-tones" x1="0" y1="0" x2="1" y2="1">
      <stop offset="0" stop-color="var(--dress-red)"/>
      <stop offset="0.35" stop-color="#b9676a"/>
      <stop offset="0.6" stop-color="var(--street-grey)"/>
      <stop offset="1" stop-color="var(--street-dark)"/>
    </linearGradient>
  </defs>

  <g class="disc" clip-path="url(#disc-shape)">
    <g class="photo-sunset" role="img" aria-label="Photo: a woman with flowing hair and open arms facing a golden sunset by the sea">
      <rect x="190" y="90" width="820" height="480" fill="url(#sunset-tones)"/>
      <rect x="190" y="90" width="820" height="480" fill="url(#sun-glow)"/>
    </g>
    <path class="photo-street" role="img" aria-label="Photo: a couple in a red dress and brown shoes picking up apples beside a bicycle on a cobbled street"
          d="M190 512 Q560 418 1010 566 L1010 910 L190 910 Z" fill="url(#street-tones)"/>
    <path class="divider-band" d="M190 500 Q560 406 1010 552" fill="none" stroke="var(--band)" stroke-width="20"/>
  </g>

  <circle class="disc-hub" cx="600" cy="500" r="125" fill="var(--backdrop)"/>
  <circle class="disc-spindle" cx="598" cy="500" r="65" fill="var(--spindle-red)"/>

  <text class="title-script title-life" x="556" y="352" font-size="158">My Life</text>
  <text class="title-script title-love" x="575" y="738" font-size="158">My Love</text>
  <text class="span-label" x="617" y="834" font-size="38">40YEAR</text>
</svg>
</body>
</html>
```